Company Website

We need an interactive website designed that for new company. Our company is in the Automotive fleet maintenance business. We have wide ranging customers in many industries e.g Aviation industry, construction industry, transportation etc.
We would like the website to have login accounts where customers can register, login and access their service history. Also we would like to have an appointment system where customers could schedule appointments, once appointments are made that time would no longer be available to be selected as it would be booked etc.

The website should also be updatable and provide areas for showcasing
Our services
Products/parts (possibly store front)
Customer feedback
Appointments
Our customers (where our customers can advertise or be showcased)
About us
Contacts
gallery

We would like designs that have a modern, corporate feel, One that is user friendly.
prefer a design that does not look like a template.

Target Market(s)

Medium to large companies, small business owners and the general motoring public.

Industry/Entity Type

Construction

Requirements
Must have
• Customer login set up so a database of customer vehicle maintenance history as well as the ability to schedule repairs via their account. They could also check the status of a repair.
Nice to have
• Photo gallery to show case current projects.
Our customers page where we can show case our clients they could also post their events on there, promotions etc.

The theme Should be something that's reflective of our core business; fleet maintenance. It would be nice to capture some sort of background in there that depicts some of that for example mixer trucks, tractors,loaders excavators forklifts cars trucks. That's what we deal with. It's up to the designer to capture the Essence of this as much as possible. Impress me.
Should not have
• Would prefer a custom website not a template.

```html
<!DOCTYPE html>
<html lang="en">
<head>
<meta charset="utf-8">
<title>Vantora Fleet &amp; Auto Maintenance</title>
<link href="https://fonts.googleapis.com/css2?family=Arimo:wght@400;700&display=swap" rel="stylesheet">
<style>
:root{
  --red:#b70f19;
  --red-dark:#8e0a12;
  --red-bright:#c8141e;
  --ink:#222;
  --muted:#555;
  --nav:#1b0707;
  --panel:#ffffff;
  --panel-soft:#ececec;
  --frame:#dcdcdc;
  --white:#fff;
}
*{margin:0;padding:0;box-sizing:border-box}
html,body{width:1200px;height:728px;overflow:hidden}
body{font-family:"Arimo",Arial,sans-serif;background:var(--red);color:var(--ink);position:relative}
.abs{position:absolute}

/* header */
.site-header{left:0;top:0;width:1200px;height:60px;background:var(--white)}
.brand{left:322px;top:14px;display:flex;align-items:center;gap:6px;color:var(--red);font-weight:700;font-size:20px;letter-spacing:1px}
.brand-mark{width:12px;height:12px;background:var(--red);border-radius:50%}
.brand-sub{left:322px;top:39px;color:var(--red);font-weight:700;font-size:7px;letter-spacing:.4px}
.login-label{left:668px;top:12px;font-size:9px;color:#333}
.login-input{top:27px;width:86px;height:15px;border:1px solid #ccc;background:#fff;font-size:7px;color:#aaa;padding:3px 4px}
.login-user{left:668px}.login-pass{left:758px}
.login-btn{left:848px;top:27px;width:35px;height:15px;background:var(--red-bright);color:#fff;font-size:9px;text-align:center;line-height:15px;border-radius:2px}

/* navigation */
.main-nav{left:0;top:60px;width:1200px;height:21px;background:var(--nav)}
.main-nav ul{list-style:none;display:flex;position:absolute;left:316px;top:0;height:21px}
.main-nav li{font-size:10px;color:#fff;line-height:21px;padding:0 7px}
.main-nav li.active{background:var(--red-bright)}

/* backdrop */
.backdrop{background:radial-gradient(ellipse at center,rgba(220,60,60,.35),rgba(160,10,20,0) 70%)}
.bg-engine{left:0;top:81px;width:340px;height:420px}
.bg-excavator{left:880px;top:81px;width:320px;height:320px;background:radial-gradient(ellipse at center,rgba(240,110,70,.45),rgba(180,20,20,0) 70%)}
.bg-pickup{left:880px;top:450px;width:320px;height:200px}

/* hero */
.hero-truck{left:316px;top:103px;width:384px;height:174px;background:linear-gradient(180deg,#f4f4f4,#d8d8d8);border-radius:40px 20px 8px 8px}
.hero-text{left:700px;top:132px;width:178px;font-size:13px;line-height:17px;color:#fff}
.hero-register{left:738px;top:211px;width:73px;height:23px;background:linear-gradient(#3a3a3a,#111);color:#fff;font-size:12px;text-align:center;line-height:23px;border-radius:2px;border:1px solid #555}

/* content panel */
.content-panel{left:316px;top:277px;width:568px;height:400px;background:var(--panel);border-radius:5px}
.section-title{font-size:13px;color:#222;font-weight:400}
.section-title em{font-style:normal;color:var(--red-bright)}
.welcome-title{left:336px;top:294px}
.welcome-copy{left:336px;top:314px;width:361px;font-size:6.4px;line-height:13px;color:var(--muted);text-align:justify}
.appointment-cta{left:715px;top:304px;width:152px;height:89px;background:linear-gradient(#444,#111);border-radius:6px;color:#fff;text-align:center;font-size:12px;line-height:16px}
.appointment-cta svg{display:block;margin:8px auto 6px}

.gallery{left:334px;top:413px;width:533px;height:141px;background:var(--panel-soft);border-radius:4px}
.gallery-title{left:345px;top:421px}
.gallery-item{top:442px;width:113px;height:95px;background:var(--frame)}
.gallery-thumb{position:absolute;left:8px;top:8px;width:97px;height:66px;background:#fff;padding:4px}
.gallery-thumb div{width:100%;height:100%}
.gallery-item span{position:absolute;left:0;right:0;top:79px;text-align:center;font-size:8.5px;color:#222}
.more-photos{left:791px;top:541px;font-size:7px;color:var(--red-bright);text-decoration:underline}

.services-title{left:336px;top:567px}
.service-thumb{top:590px;width:80px;height:59px;border-radius:5px;border:1px solid #ccc}
.service-copy{top:590px;width:100px;font-size:7px;line-height:9.5px;color:var(--muted)}
.service-copy strong{display:block;font-weight:400;font-size:9.5px;color:#333;margin-bottom:3px}
.service-divider{left:526px;top:590px;width:1px;height:60px;background:#ddd}

.feedback-title{left:752px;top:570px}
.feedback-box{left:731px;top:588px;width:136px;height:64px;background:var(--panel-soft);border-radius:4px}
.feedback-avatar{position:absolute;left:8px;top:17px;width:28px;height:30px;background:#999}
.feedback-copy{position:absolute;left:42px;top:16px;width:88px;font-size:6.5px;line-height:8.5px;color:var(--muted)}
.quote{position:absolute;font-size:14px;color:#aaa;font-family:Georgia,serif}

/* footer */
.footer-links{left:0;top:689px;width:1200px;text-align:center;font-size:7px;color:#fff}
.copyright{left:0;top:707px;width:1200px;text-align:center;font-size:7px;color:#fff}
</style>
</head>
<body>

<div class="abs backdrop bg-engine" role="img" aria-label="Faint photo of an engine block"></div>
<div class="abs bg-excavator" role="img" aria-label="Faint photo of an orange excavator"></div>
<div class="abs backdrop bg-pickup" role="img" aria-label="Faint photo of a pickup truck"></div>

<header class="abs site-header">
  <div class="abs brand"><span class="brand-mark"></span>VANTORA</div>
  <div class="abs brand-sub">FLEET &amp; AUTO MAINTENANCE</div>
  <div class="abs login-label">Login</div>
  <div class="abs login-input login-user">Username</div>
  <div class="abs login-input login-pass">Password</div>
  <div class="abs login-btn">Login</div>
</header>

<nav class="abs main-nav">
  <ul>
    <li class="active">Home</li><li>About us</li><li>Our services</li><li>Products/Parts</li><li>Gallery</li><li>Appointments</li><li>Our Customers</li><li>Customer Feedback</li><li>Contacts</li>
  </ul>
</nav>

<div class="abs hero-truck" role="img" aria-label="Photo of a white service truck with a mounted crane"></div>
<p class="abs hero-text">Lorem Ipsum is simply dummy text of the printing and type-setting industry. Lorem Ipsum has been the industry's stan-</p>
<div class="abs hero-register">Register</div>

<main class="abs content-panel"></main>

<h2 class="abs section-title welcome-title">Welcome to <em>Vantora</em></h2>
<p class="abs welcome-copy">Lorem Ipsum is simply dummy text of the printing and typesetting industry. Lorem Ipsum has been the industry's standard dummy text ever since the 1500s, when an unknown printer took a galley of type and scrambled it to make a type specimen book. It has survived not only five centuries, but also the leap into electronic typesetting, remaining essentially unchanged. It was popularised in the 1960s with the release of Lettaform sheets containing Lorem Ipsum passages, and more recently with desktop publishing software like Pagewright including versions of Lorem Ipsum. Lorem Ipsum is simply dummy text of the printing and typesetting industry. Lorem Ipsum has been the indus-</p>

<div class="abs appointment-cta">
  <svg width="36" height="30" viewBox="0 0 36 30" aria-hidden="true">
    <rect x="1" y="3" width="28" height="24" rx="2" fill="#eee" stroke="#999"/>
    <rect x="1" y="3" width="28" height="6" fill="#7a8fb0"/>
    <g fill="#bbb"><rect x="5" y="12" width="4" height="3"/><rect x="11" y="12" width="4" height="3"/><rect x="17" y="12" width="4" height="3"/><rect x="5" y="18" width="4" height="3"/><rect x="11" y="18" width="4" height="3"/></g>
    <circle cx="26" cy="20" r="8" fill="#fff" stroke="#888" stroke-width="1.5"/>
    <path d="M26 15v5l3 2" stroke="#333" stroke-width="1.3" fill="none"/>
  </svg>
  Click Here to Make an<br>Appointment Online
</div>

<section class="abs gallery"></section>
<h2 class="abs section-title gallery-title">Photo <em>Gallery</em></h2>
<div class="abs gallery-item" style="left:353px"><div class="gallery-thumb"><div role="img" aria-label="Photo of a yellow mixer truck" style="background:linear-gradient(#cfd6e2,#c9b640)"></div></div><span>Mixer Trucks</span></div>
<div class="abs gallery-item" style="left:482px"><div class="gallery-thumb"><div role="img" aria-label="Photo of a red tractor" style="background:linear-gradient(#dfe6ee,#a63a30)"></div></div><span>Tractors</span></div>
<div class="abs gallery-item" style="left:611px"><div class="gallery-thumb"><div role="img" aria-label="Photo of an orange loader excavator" style="background:linear-gradient(#f2f2f2,#d9642a)"></div></div><span>Loaders Excavators</span></div>
<div class="abs gallery-item" style="left:738px"><div class="gallery-thumb"><div role="img" aria-label="Photo of a yellow truck" style="background:linear-gradient(#f2f2f2,#e0b82a)"></div></div><span>Trucks</span></div>
<div class="abs more-photos">More Photos...</div>

<h2 class="abs section-title services-title">Our <em>Services</em></h2>
<div class="abs service-thumb" style="left:341px;background:linear-gradient(#e8e8e8,#7a8594)" role="img" aria-label="Photo of a turbocharger"></div>
<p class="abs service-copy" style="left:428px"><strong>Lorem Ipsum is simply</strong>Lorem Ipsum is simply dummy text of the printing and typesetting industry. Lorem Ipsum has been the</p>
<div class="abs service-divider"></div>
<div class="abs service-thumb" style="left:537px;background:linear-gradient(#3b4a5c,#1d2430)" role="img" aria-label="Photo of a diesel engine"></div>
<p class="abs service-copy" style="left:623px"><strong>Lorem Ipsum is simply</strong>Lorem Ipsum is simply dummy text of the printing and typesetting industry. Lorem Ipsum has been the</p>

<h2 class="abs section-title feedback-title">Customer <em>feedback</em></h2>
<div class="abs feedback-box">
  <span class="quote" style="left:5px;top:2px">&ldquo;</span>
  <div class="feedback-avatar" role="img" aria-label="Customer avatar placeholder"></div>
  <p class="feedback-copy">Lorem Ipsum is simply dummy text of the printing and typesetting industry. Lorem Ipsum has been the</p>
  <span class="quote" style="right:5px;bottom:-4px">&rdquo;</span>
</div>

<footer>
  <p class="abs footer-links">Home &nbsp;|&nbsp; About us &nbsp;|&nbsp; Our services &nbsp;|&nbsp; Products/Parts &nbsp;|&nbsp; Gallery &nbsp;|&nbsp; Appointments &nbsp;|&nbsp; Our Customers &nbsp;|&nbsp; Customer Feedback &nbsp;|&nbsp; Contacts</p>
  <p class="abs copyright">Copyright &copy; 2013 Vantora . All rights reserved.</p>
</footer>

</body>
</html>
```